The Harrowgate Ledger Summit. A Summit For Ledger Keepers...By Ledger Keepers.
The Harrowgate Ledger Summit was created to provide quality content at a reasonable price-point to allow organizations to send multiple attendees and encourage active participation. This event is intended for debt collection professionals who are:

Senior Level Executives
Front Line Collection Managers
Compliance Professionals
Trainers
While there are many great conferences within our industry to choose from, most collection conferences just scratch the surface when attempting to provide real world solutions. The Harrowgate Ledger Summit was created to provide debt collection professionals with a foundation of direction, insight, and actionable solutions that can be applied regardless of the size of an organization. Join us at the inaugural Harrowgate Ledger Summit as we assemble an expert team of operations, compliance, and training professionals that will deep dive into real world solutions for today’s real world debt collection issues. Here is what you can expect:

Solution driven sessions, not sponsor driven sessions
Substance from "In The Trenches" experts who live it, breathe it, work it...every day
Learn operational, compliance, and training strategies that have proven success
Understand how to efficiently and effectively manage YOUR resources
Apply state of the art technology solutions

Target Market(s)

Debt collection agencies and creditors

Industry/Entity Type

Financial Service

Font styles to use
Serif

Requirements
Must have
• link to website www.HLS2016.example and use of image provided HLSCover. Use same color scheme as the HLSCover image

```html
<!DOCTYPE html>
<html lang="en">
<head>
<meta charset="utf-8">
<title>Harrowgate Ledger Summit 2016 – Postcard</title>
<link rel="stylesheet" href="https://fonts.googleapis.com/css2?family=Josefin+Sans:wght@300;400&family=Open+Sans:wght@400;600;700&family=Roboto+Condensed:wght@700&display=swap">
<style>
  :root{
    --teal:#2bb6c4;
    --teal-deep:#1d8f9c;
    --lime:#d3e05a;
    --lime-deep:#b9c93b;
    --charcoal:#2a2a2b;
    --ink:#1b1b1b;
    --paper:#f4f4f4;
    --backdrop:#ecebe8;
    --white:#ffffff;
  }
  *{box-sizing:border-box;margin:0;padding:0}
  html,body{width:1200px;height:1200px;overflow:hidden}
  body{background:var(--backdrop);position:relative;font-family:"Open Sans",Arial,sans-serif}

  /* ---------- mailing side ---------- */
  .mailer{position:absolute;left:170px;top:50px;width:860px;height:520px;background:var(--paper);overflow:hidden;box-shadow:0 4px 18px rgba(0,0,0,.18);isolation:isolate}
  .mailer__skyline{position:absolute;inset:0;background:linear-gradient(180deg,#fafafa 0%,#eeeeee 45%,#d6d6d6 78%,#e8e8e8 100%)}
  .mailer__panel{position:absolute;inset:0;background:var(--charcoal);clip-path:polygon(0 0,500px 0,380px 520px,0 520px)}
  .postage{position:absolute;right:80px;top:24px;width:124px;height:124px;border:2px solid var(--ink);display:flex;align-items:center;justify-content:center;font:700 12px "Open Sans",Arial,sans-serif;color:var(--ink);letter-spacing:.5px}
  .intro{position:absolute;left:40px;top:36px;width:400px;font-size:9.6px;line-height:13px;color:#d8d8d8;text-align:justify}
  .audience{position:absolute;left:0;top:100px;list-style:none;z-index:1;isolation:isolate}
  .audience__item{position:relative;height:28px;margin-bottom:3px;padding-left:28px;font:700 19px/28px "Roboto Condensed",Arial,sans-serif;color:var(--white);letter-spacing:.3px}
  .audience__item::after{content:"";position:absolute;left:18px;top:0;height:28px;width:var(--w);background:linear-gradient(90deg,var(--teal-deep),var(--teal) 55%,rgba(43,182,196,0));z-index:0}
  .audience__item::before{content:"";position:absolute;left:0;top:0;width:24px;height:28px;background:var(--lime);clip-path:polygon(0 0,100% 50%,0 100%);z-index:1}
  .audience__item span{position:relative;z-index:2}
  .invite{position:absolute;left:40px;top:228px;width:380px;font-size:9.6px;line-height:13px;color:#d8d8d8}
  .expect{position:absolute;left:28px;top:290px;width:320px;list-style:none}
  .expect li{position:relative;padding-left:10px;margin-bottom:5px;font:700 10.6px/14px "Open Sans",Arial,sans-serif;color:var(--white)}
  .expect li::before{content:"";position:absolute;left:0;top:5px;width:4px;height:4px;background:var(--teal)}
  .details{position:absolute;left:0;top:440px;width:430px;height:52px;background:var(--lime);clip-path:polygon(0 0,100% 0,96% 100%,0 100%);display:flex;color:var(--ink)}
  .details__block{display:flex;align-items:center;gap:8px;padding-left:22px;font-size:9.2px;line-height:11.5px}
  .details__block--where{width:200px;border-right:1px solid rgba(0,0,0,.35)}
  .details__label{writing-mode:vertical-rl;transform:rotate(180deg);font:700 8.5px "Open Sans",Arial,sans-serif;color:var(--teal-deep);letter-spacing:1.5px}
  .moreinfo{position:absolute;left:28px;top:498px;font:700 10px "Open Sans",Arial,sans-serif;color:var(--teal);letter-spacing:1px}
  .moreinfo b{color:var(--white);font-size:11.5px;letter-spacing:.5px;margin-left:4px}

  /* ---------- cover side ---------- */
  .cover{position:absolute;left:390px;top:610px;width:420px;height:560px;overflow:hidden;box-shadow:0 4px 18px rgba(0,0,0,.22)}
  .cover__art{position:absolute;inset:0;background:
      linear-gradient(200deg,rgba(43,182,196,0) 35%,rgba(43,182,196,.55) 60%,rgba(211,224,90,.6) 85%),
      linear-gradient(180deg,#8a8a8a 0%,#a8a8a8 30%,#5e5e5e 55%,#2c2c2c 100%)}
  .identity{position:absolute;left:120px;top:380px;width:290px}
  .identity__name{display:flex;align-items:flex-start;gap:12px;border-left:1px solid rgba(255,255,255,.7);padding-left:12px}
  .identity__mark{width:14px;height:14px;background:var(--white);margin-top:6px;flex:none}
  .identity__title{font:300 24px/26px "Josefin Sans",Arial,sans-serif;color:var(--white);letter-spacing:3px;text-transform:uppercase}
  .identity__tag{margin:6px 0 0 13px;font-size:8.4px;color:#e6e6e6}
  .identity__where{margin-top:14px;font:700 13px/15px "Open Sans",Arial,sans-serif;color:var(--white);text-transform:uppercase}
</style>
</head>
<body>

<section class="mailer">
  <div class="mailer__skyline" role="img" aria-label="Faded photograph of the riverfront arch and city skyline"></div>
  <div class="mailer__panel"></div>
  <div class="postage">POSTAGE</div>

  <p class="intro">The Harrowgate Ledger Summit was created to provide quality content at a reasonable price-point to allow organizations to send multiple attendees and encourage active participation. This event is intended for debt collection professionals who are:</p>

  <ul class="audience">
    <li class="audience__item" style="--w:330px"><span>SENIOR LEVEL EXECUTIVES</span></li>
    <li class="audience__item" style="--w:400px"><span>FRONT LINE COLLECTION MANAGERS</span></li>
    <li class="audience__item" style="--w:360px"><span>COMPLIANCE PROFESSIONALS</span></li>
    <li class="audience__item" style="--w:260px"><span>TRAINERS</span></li>
  </ul>

  <p class="invite">Join us at the inaugural Harrowgate Ledger Summit as we assemble an expert team of operations, compliance, and training professionals that will deep dive into real world solutions for today’s real world debt collection issues. Here is what you can expect:</p>

  <ul class="expect">
    <li>Solution driven sessions, not sponsor driven sessions</li>
    <li>Substance from "In The Trenches" experts who live it, breathe it, work it...every day</li>
    <li>Learn operational, compliance, and training strategies that have proven success</li>
    <li>Understand how to efficiently and effectively manage YOUR resources</li>
    <li>Apply state of the art technology solutions</li>
  </ul>

  <div class="details">
    <div class="details__block details__block--where">
      <span class="details__label">WHERE</span>
      <p>Riverbend Meridian Hotel<br>One Riverbend Blvd.<br>Saint Charles, Missouri 63301<br>(555) 014-2290</p>
    </div>
    <div class="details__block">
      <span class="details__label">WHEN</span>
      <p>Monday, March 21, 2016 thru<br>Wednesday, March 23, 2016<br>8:00 AM - 12:00 PM<br>Central Time</p>
    </div>
  </div>

  <p class="moreinfo">FOR MORE INFORMATION VISIT <b>www.HLS2016.example</b></p>
</section>

<section class="cover">
  <div class="cover__art" role="img" aria-label="Black and white riverfront photograph with overlaid teal and lime geometric artwork"></div>
  <div class="identity">
    <div class="identity__name">
      <span class="identity__mark"></span>
      <p class="identity__title">Harrowgate<br>Ledger<br>Summit 2016</p>
    </div>
    <p class="identity__tag">A Summit For Ledger Keepers...By Ledger Keepers.</p>
    <p class="identity__where">Saint Louis, Missouri<br>March 21, 2016 - March 23, 2016</p>
  </div>
</section>

</body>
</html>
```